Flyer-Design für den Bereich Familienfotografie
Helene hat hervorragende Arbeit geleistet. Der erste Wurf war schon überzeugend. Änderungswünsche zum finalen Design wurden schnell und gut umgesetzt und besonders gefallen haben mir die von ihr proaktiv eingebrachten Ideen und Lösungsvorschläge. Vielen Dank!
Zielgruppe
Ich bin ein Fotograf mit dem Schwerpunkt Familienfotos und Reportagen
Aufgabenstellung
Hier soll ein Flyer für den Bereich Familienfotografie entstehen. Also Schwangerschaft, Baby, Familien, Portrait & Pärchen. Er soll Infos zu meinem Leistungsumfang und zum Ablauf von Buchungen, Shootings und Bildauswahl transtportieren. Hier gerne erstmal Blindtext vorsehen, ich liefere dann Inhalt nach.
Infos und weitere Eindrücke gibts auf www.bernhardlossow.de
Die beigefügten Bilder müssen natürlich nicht alle genutzt werden, vor Erstellung der Druckdaten suche ich die Bilder auch noch ohne Logo und in einer höheren Auflösung heraus, zur Gestaltung sollte das aber reichen.
Als Format wäre Din lang hochkant mit 6-8 Seiten ganz schön, (wegen Postversand im Brief/Rechnungsumschlag). Wenn Ihr gute Gründe für anderes liefert, lassen ich mich aber sicher auch überzeugen.
Optisch soll der Flyer schon auffallen, also etwas mehr als ein paar Fotos und Text drauffallen lassen, bitte aber kein verschnörkelter pastell 'Schi-Schi' wie er immer mal wieder aus dem anglophonen Raum zu uns schwappt ;)
Ich freue mich auf Eure Ideen!
Im Nachgang zu diesem Projekt sollen dann auf der Basis noch Flyer für Hochzeiten und Reportagen erstellt werden, sowie in 2019 auch neue Visitenkarten und ein Portfolio-Booklet. Diese Aufträge gehen dann natürlich auch an den oder diejenige, die sich bei dem 'Familienflyer' durchsetzt.
Falls Fragen oder Unklarheiten aufkommen, lasst es mich gerne wissen! Kontaktdaten findet Ihr auf meiner Seite.
Generell habe ich mich vielleicht noch nicht klar genug ausgedrückt (sorry, ist mein erstes Projekt hier)
Der Flyer soll natürlich die Wertigkeit und Professionalität meiner Arbeit widerspiegeln. Ganz klar soll er NICHT so aussehen, als hätte man das Ganze in 3 min in Powerpoint zusammengeklickt.
Es muss direkt klar werden, dass es in dem Flyer um die Familienfotografie geht und es sollen alle 4 Bereiche (Schwangerschaft, Baby, Familien, Portraits/Pärchen) darges..

```html
<!DOCTYPE html>
<html lang="de">
<head>
<meta charset="utf-8">
<title>Bernhard Lossow Fotografie – Flyer Innenseite</title>
<link href="https://fonts.googleapis.com/css2?family=Arimo:wght@400;700&display=swap" rel="stylesheet">
<style>
  :root {
    --band: #555555;
    --paper: #ffffff;
    --ink: #000000;
    --heading-grey: #444444;
    --body-grey: #333333;
    --wedding-green: #4f6b3a;
    --wedding-light: #d9ddd4;
    --child-dark: #1e1a1c;
    --child-warm: #c98a2e;
  }
  html, body {
    margin: 0;
    padding: 0;
    overflow: hidden;
    background: var(--paper);
  }
  .flyer {
    position: relative;
    width: 1200px;
    height: 927px;
    overflow: hidden;
    background: var(--paper);
    font-family: "Arimo", Arial, sans-serif;
    color: var(--ink);
  }
  .band { position: absolute; left: 0; width: 1200px; background: var(--band); }
  .band--top { top: 0; height: 38px; }
  .band--bottom { bottom: 0; height: 35px; }

  .section-title {
    position: absolute; left: 64px; top: 77px;
    margin: 0; padding-left: 14px;
    border-left: 4px solid var(--ink);
    font-size: 25px; font-weight: 700; line-height: 30px;
  }

  .service { position: absolute; left: 118px; width: 200px; }
  .service__photo { width: 178px; height: 178px; border-radius: 50%; margin-left: 0; }
  .service__photo--wedding {
    background: radial-gradient(circle at 45% 60%, var(--wedding-light) 0%, #8fa07a 38%, var(--wedding-green) 70%, #223018 100%);
  }
  .service__photo--report {
    background: radial-gradient(circle at 50% 50%, var(--child-warm) 0%, #8a5a22 40%, var(--child-dark) 80%);
  }
  .service__name {
    margin: 0; font-size: 21px; font-weight: 700; line-height: 26px;
    padding-bottom: 14px; border-bottom: 4px solid var(--ink); width: 140px;
  }
  .service__text {
    margin: 12px 0 0; width: 170px;
    font-size: 11.5px; line-height: 16px; color: var(--body-grey);
    word-break: break-all;
  }
  .service--wedding { top: 137px; }
  .service--wedding .service__name { margin: 8px 0 0 18px; }
  .service--wedding .service__text { margin-left: 17px; }
  .service--report { top: 514px; }
  .service--report .service__name { margin: 8px 0 0 13px; }
  .service--report .service__text { margin-left: 12px; }

  .booking-title {
    position: absolute; left: 463px; top: 136px; margin: 0;
    font-size: 36px; font-weight: 700; line-height: 50px; color: var(--heading-grey);
  }
  .booking-rule { position: absolute; left: 467px; top: 361px; width: 325px; height: 5px; background: var(--ink); }
  .contact {
    position: absolute; left: 466px; top: 395px; margin: 0;
    font-size: 14.5px; font-weight: 700; line-height: 21px; font-style: normal;
  }
  .contact p { margin: 0; }
  .contact .contact__line { margin-top: 20px; }
  .contact .contact__line--first { margin-top: 38px; }

  .brand {
    position: absolute; display: flex; flex-direction: column; align-items: flex-start;
    font-weight: 700; color: var(--ink);
  }
  .brand__dot { border-radius: 50%; background: var(--ink); }
  .brand__name { letter-spacing: 2px; line-height: 1.1; }
  .brand__sub { letter-spacing: 1px; align-self: flex-end; line-height: 1.2; }
  .brand--large { left: 824px; top: 236px; width: 358px; }
  .brand--large .brand__dot { width: 80px; height: 80px; margin-bottom: 30px; }
  .brand--large .brand__name { font-size: 30px; }
  .brand--large .brand__sub { font-size: 26px; }
  .brand--small { left: 470px; top: 668px; width: 282px; }
  .brand--small .brand__dot { width: 64px; height: 64px; margin-bottom: 20px; }
  .brand--small .brand__name { font-size: 23px; }
  .brand--small .brand__sub { font-size: 20px; margin-right: 4px; }

  .focus-list {
    position: absolute; left: 867px; top: 471px; margin: 0;
    padding: 0 0 0 15px; list-style: none;
    border-left: 4px solid var(--ink);
    font-size: 26px; font-weight: 700; line-height: 37.5px;
  }
</style>
</head>
<body>
<main class="flyer">
  <div class="band band--top"></div>

  <h2 class="section-title">weitere Leistungen</h2>

  <section class="service service--wedding">
    <div class="service__photo service__photo--wedding" role="img" aria-label="Foto: Brautpaar Hand in Hand im Grünen"></div>
    <h3 class="service__name">Hochzeit</h3>
    <p class="service__text">BlindtextBlindtextBlindtextBlindtextBlindtextBlindtextBlindtextBlindtextBlindtextBlindtextBlindtextBlindtextBlindtextBlindtextBlindtextBlindtextBlindtextBlindtextBlindtextBlindtext</p>
  </section>

  <section class="service service--report">
    <div class="service__photo service__photo--report" role="img" aria-label="Foto: fröhliches Kind im Sessel"></div>
    <h3 class="service__name">Reportage</h3>
    <p class="service__text">BlindtextBlindtextBlindtextBlindtextBlindtextBlindtextBlindtextBlindtextBlindtextBlindtextBlindtextBlindtextBlindtextBlindtextBlindtextBlindtextBlindtextBlindtextBlindtextBlindtext</p>
  </section>

  <h2 class="booking-title">Buchung und<br>weitere<br>Informationen<br>unter:</h2>
  <div class="booking-rule"></div>

  <address class="contact">
    <p>Bernhard Lossow |</p>
    <p>Lindenhofweg 12 |</p>
    <p>21423 Moorhagen |</p>
    <p class="contact__line contact__line--first">Tel: 04170 – 48 20 316</p>
    <p class="contact__line">Mob: 0151 - 27 64 83 05</p>
    <p class="contact__line">E-Mail: kontakt@bernhardlossow.de</p>
  </address>

  <div class="brand brand--large">
    <span class="brand__dot"></span>
    <span class="brand__name">BERNHARDLOSSOW</span>
    <span class="brand__sub">fotografie</span>
  </div>

  <div class="brand brand--small">
    <span class="brand__dot"></span>
    <span class="brand__name">BERNHARDLOSSOW</span>
    <span class="brand__sub">fotografie</span>
  </div>

  <ul class="focus-list">
    <li>Familie</li>
    <li>Portrait</li>
    <li>Schwangerschaft</li>
    <li>Baby</li>
    <li>Paar</li>
  </ul>

  <div class="band band--bottom"></div>
</main>
</body>
</html>
```